one side yoga classes, other side rental log cabin

I need a flyer to advertise yoga classes on a lake , and to describe the various styles of classes, and who they can benefit, Days Times .prices
Linked to it is a rental log cabin that can be rented privetly to families or Groups (8 max) www.staysbycalderbrook.com This also is rented to yoga teacher that would like to Hire Cabin and the Studio www.velinoretreat.co.uk or
for Holistic weekends.

Teacher

```html
<!DOCTYPE html>
<html lang="en">
<head>
<meta charset="utf-8">
<title>Velino Lodge &amp; Retreat Flyers</title>
<link rel="stylesheet" href="https://fonts.googleapis.com/css2?family=Roboto:wght@300;400;700&family=Roboto+Condensed:wght@400&family=Yesteryear&family=Josefin+Sans:wght@300&family=Cormorant+Garamond:wght@400&display=swap">
<style>
:root{
  --bg:#1d1d1d;
  --green:#009a73;
  --green-dark:#0b7a5b;
  --mint:#a9dbd2;
  --mint-pale:#dcefe9;
  --teal-line:#8fcfc6;
  --red:#d8262e;
  --ink:#111;
  --purple:#4a1c47;
  --purple-mid:#6a2f66;
  --cream:#f6f0e4;
  --grey-text:#b7a9b6;
  --white:#fff;
}
*{margin:0;padding:0;box-sizing:border-box}
html,body{width:1200px;height:1015px;overflow:hidden;background:var(--bg)}
.stage{position:relative;width:1200px;height:1015px}

/* Back flyer: yoga retreat */
.retreat-card{position:absolute;left:201px;top:270px;width:909px;height:644px;
  background:linear-gradient(180deg,#f3eef3 0%,var(--cream) 60%,#efe2c9 70%);overflow:hidden;
  font-family:"Roboto",sans-serif}
.retreat-card .top-strip{position:absolute;left:0;top:0;width:100%;height:22px;
  background:linear-gradient(90deg,var(--purple),var(--purple-mid))}
.retreat-title{position:absolute;right:31px;font-family:"Cormorant Garamond",serif;
  font-size:38px;color:#5b4a5a;line-height:1;white-space:nowrap}
.retreat-title.l1{top:52px;right:53px}
.retreat-title.l2{top:104px}
.studio-bar{position:absolute;left:0;top:163px;width:100%;height:28px;background:var(--purple-mid);
  color:var(--white);font-size:22px;line-height:28px;text-align:right;padding-right:47px}
.rule{position:absolute;left:40px;right:11px;height:1px;background:#6a3a66}
.venue{position:absolute;right:20px;top:364px;font-size:18px;color:#222}
.retreat-base{position:absolute;left:0;top:440px;width:100%;height:204px;
  background:linear-gradient(160deg,#3d1638,#5a2455 60%,#46183f)}
.brand-name{position:absolute;left:60px;top:86px;font-family:"Roboto",sans-serif;font-weight:300;
  font-size:50px;letter-spacing:6px;color:#e6e0e6}
.retreat-info{position:absolute;left:373px;top:40px;color:var(--grey-text);font-size:18px;line-height:27px}
.retreat-phones{position:absolute;left:373px;top:96px;font-family:"Roboto Condensed",sans-serif;
  font-size:42px;color:var(--white);white-space:nowrap}
.retreat-web{position:absolute;left:375px;top:154px;font-size:18px;font-weight:700;letter-spacing:4px;color:var(--white)}

/* Front flyer: lodge rental */
.lodge-card{position:absolute;left:86px;top:101px;width:910px;height:645px;background:var(--mint-pale);
  overflow:hidden;font-family:"Roboto",sans-serif}
.headline-band{position:absolute;left:0;top:16px;width:100%;height:127px;
  background:linear-gradient(90deg,var(--green-dark),var(--green) 15%,var(--green) 85%,var(--green-dark));
  color:var(--white);text-align:center;padding-top:12px}
.headline-band .lead{font-size:26px;line-height:34px}
.headline-band .main{font-size:30px;font-weight:700;line-height:37px}
.lodge-photo{position:absolute;left:0;top:143px;width:650px;height:502px;
  background:linear-gradient(180deg,#eef2f3 0%,#c9a48c 14%,#7a4f3a 30%,#4e3327 52%,#8a7a6a 66%,#c8dcd6 80%,var(--mint) 100%)}
.lodge-name{position:absolute;left:90px;top:445px;font-family:"Josefin Sans",sans-serif;font-weight:300;
  font-size:56px;letter-spacing:3px;color:var(--white);text-transform:uppercase;white-space:nowrap}
.contact-box{position:absolute;left:21px;top:521px;width:608px;height:102px;background:var(--green);
  text-align:center}
.contact-box .phones{font-size:31px;color:var(--white);padding-top:16px;line-height:38px}
.contact-box .web{font-size:24px;letter-spacing:2.5px;color:#0e1e19;margin-top:6px}
.info-panel{position:absolute;left:566px;top:143px;width:344px;height:502px;text-align:center;
  background:linear-gradient(180deg,#fff 0%,#fbfdfc 55%,#e4f3ef 80%,var(--mint) 100%)}
.info-panel svg{position:absolute;left:0;top:0}
.welcome{position:absolute;left:0;width:328px;top:8px;font-family:"Yesteryear",cursive;font-size:44px;
  color:var(--red);white-space:nowrap;text-align:center}
.region{position:absolute;left:0;width:328px;top:66px;font-size:27px;text-align:center;color:var(--ink)}
.divider{position:absolute;height:1px;background:var(--red);opacity:.55}
.body-copy{position:absolute;left:0;width:328px;font-size:17px;line-height:22.6px;text-align:center;color:var(--ink)}
.body-copy.red{color:var(--red)}
</style>
</head>
<body>
<div class="stage">

  <section class="retreat-card" aria-label="Velino Retreat yoga flyer">
    <div class="top-strip"></div>
    <div class="retreat-title l1">Yoga by the Lakeside</div>
    <div class="retreat-title l2">in Norfolk</div>
    <div class="studio-bar">LAKE YOGA STUDIO</div>
    <div class="rule" style="top:241px"></div>
    <div class="rule" style="top:311px"></div>
    <div class="rule" style="top:355px"></div>
    <div class="venue">Thursdays 7pm (Memorial Hall)</div>
    <div class="rule" style="top:395px"></div>
    <div class="retreat-base">
      <div class="brand-name">VELINO</div>
      <div class="retreat-info">Velino Retreat<br>4 Ashwell Lakes, Ashwell. PE99 1ZZ</div>
      <div class="retreat-phones">01632 960 294 • 07700 900 026</div>
      <div class="retreat-web">www.velinoretreat.co.uk</div>
    </div>
  </section>

  <section class="lodge-card" aria-label="Velino Lodge rental flyer">
    <header class="headline-band">
      <div class="lead">If you are looking to escape to the country for a short break</div>
      <div class="main">Then our Modern, Spacious Cabin in the Heart of Norfolk<br>could be Exactly what you are Looking for</div>
    </header>

    <div class="lodge-photo" role="img" aria-label="Photograph of the log cabin with tiled roof, veranda and log fence, with an Available On Rent sign"></div>
    <div class="lodge-name">Velino Lodge</div>

    <div class="contact-box">
      <div class="phones">01632 960 294 • 07700 900 026</div>
      <div class="web">www.staysbycalderbrook.com</div>
    </div>

    <div class="info-panel">
      <svg width="344" height="502" viewBox="0 0 344 502" aria-hidden="true">
        <path d="M30 150 C 20 200, 10 250, 4 300 C 10 340, 28 380, 26 440 C 24 470, 14 490, 10 502" fill="none" stroke="var(--teal-line)" stroke-width="5"/>
        <path d="M298 150 C 308 200, 318 250, 324 300 C 318 340, 300 380, 302 440 C 304 470, 314 490, 318 502" fill="none" stroke="var(--teal-line)" stroke-width="5"/>
      </svg>
      <div class="welcome">Welcome to Holidays</div>
      <div class="region">In Norfolk!</div>
      <div class="divider" style="left:124px;width:80px;top:117px"></div>
      <div class="body-copy" style="top:128px">Outfitted with<br>All the Modern Luxuries<br>you would expect so<br>you can Relax in Comfort!</div>
      <div class="divider" style="left:92px;width:144px;top:230px"></div>
      <div class="body-copy red" style="top:249px">Rented Privetly to<br>Families or Groups (8 max)</div>
      <div class="divider" style="left:92px;width:144px;top:292px"></div>
      <div class="body-copy" style="top:310px">We also offer retreats for<br>any groups looking to<br>really relax and enjoy<br>a weekend of<br>meditation and yoga<br>in a studio suspended<br>over the lake itself</div>
      <div class="divider" style="left:118px;width:92px;top:471px"></div>
    </div>
  </section>

</div>
</body>
</html>
```